Flyer Design

We need a flyer design for a small business in Belrose NSW called "Harbor Stride Gym". We are a personal training studio. Our service includes: one on one consultation, assessment, a personalised program, personal training.We would like to include the colours as seen in the logo.The flyer design should communicate personalised care in health and fitness.

Target Market(s)

30-80 years, male and female

Industry/Entity Type

Business

Font styles to use
Sans Serif

Requirements
Must have
• Motivating image. Motivating words.

```html
<!DOCTYPE html>
<html lang="en">
<head>
<meta charset="utf-8">
<title>Harbor Stride Gym – Flyer</title>
<link href="https://fonts.googleapis.com/css2?family=Open+Sans:wght@300;400;600;700&family=Oswald:wght@500;700&family=Dancing+Script:wght@500;700&display=swap" rel="stylesheet">
<style>
:root{
  --backdrop:#87592f;
  --paper:#f7f7f7;
  --paper-grey:#e9eaeb;
  --green:#6a9a2a;
  --green-light:#8ab83e;
  --green-dark:#2f5e14;
  --green-deep:#294e10;
  --green-text:#5b9a2b;
  --ink:#3a3a3a;
  --ink-soft:#555;
  --script-red:#e4473c;
  --white:#fff;
}
*{margin:0;padding:0;box-sizing:border-box}
html,body{width:1200px;height:867px;overflow:hidden;background:var(--backdrop)}
body{position:relative;font-family:"Open Sans",Arial,sans-serif;color:var(--ink)}
.page{position:absolute;top:79px;width:504px;height:711px;overflow:hidden}
.page--info{left:64px;background:var(--paper)}
.page--cover{left:602px;background:var(--paper-grey)}
.abs{position:absolute}

/* info page */
.site-url{left:0;width:100%;top:20px;text-align:center;font-weight:700;font-size:16px;letter-spacing:1.4px;color:var(--green)}
.photo{top:50px;width:149px;height:112px;border-radius:6px}
.photo--physio{left:23px;background:linear-gradient(135deg,#c8322a 0%,#d9d9d9 55%,#f2f2f2 100%)}
.photo--lifting{left:178px;background:linear-gradient(135deg,#1c1c1c 0%,#6b5a4d 55%,#2a2a2a 100%)}
.photo--food{left:332px;background:linear-gradient(160deg,#f0eee8 0%,#9fa39c 45%,#d8a431 70%,#7a4f2a 100%)}
.bio{width:206px;font-size:9.6px;line-height:12.9px;font-weight:300;text-align:justify;color:var(--ink)}
.bio p+p{margin-top:8px}
.bio--owner{left:23px;top:181px}
.bio--specialist{left:251px;top:181px;width:226px}
.illus-woman{left:24px;top:377px;width:232px;height:192px;border-radius:50% 50% 20% 20%;background:radial-gradient(ellipse at 50% 45%,#f2b5cf 0%,#e9d9df 45%,rgba(235,235,235,0) 72%)}
.tagline{left:260px;top:406px;font-family:"Dancing Script",cursive;font-weight:700;font-size:17px;color:var(--script-red);white-space:nowrap}
.brand{left:232px;top:468px;display:flex;align-items:center;gap:8px;font-weight:600;font-size:23px;color:var(--green);white-space:nowrap}
.brand__dot{width:14px;height:14px;border-radius:50%;background:var(--green)}
.pitch{left:24px;top:578px;width:226px;text-align:center;font-size:11.2px;line-height:18.4px;color:var(--ink)}
.contact{left:270px;top:548px;width:232px;text-align:center}
.contact__label{font-size:18px;color:var(--ink)}
.contact__phone{font-size:17px;line-height:23px;color:var(--green-deep)}
.contact__mail{margin-top:8px;font-size:10.5px;line-height:17px;color:var(--ink-soft)}
.contact__rule{margin:5px auto 3px;width:172px;border-top:1px solid #bbb}
.contact__addr{font-size:11.5px;color:var(--ink-soft)}

/* cover page */
.hero{left:0;top:0;width:504px;height:370px}
.hero-photo{left:0;top:0;width:504px;height:370px}
.hero-script{left:22px;top:20px;font-family:"Dancing Script",cursive;font-weight:500;font-size:23px;line-height:27px;color:var(--white)}
.cover-brand{left:190px;top:108px;font-weight:700;font-size:23px;line-height:26px;color:var(--green)}
.headline{left:30px;top:216px;width:180px;text-align:center;font-family:"Oswald",Arial,sans-serif;font-weight:700;font-size:25px;line-height:28px;color:var(--green-deep);text-transform:uppercase}
.hours{left:434px;top:185px;width:56px;text-align:center;font-size:16px;line-height:21.3px;font-weight:300;color:var(--white)}
.badge{left:334px;top:297px;width:104px;height:104px;border-radius:50%;background:var(--white);border:4px solid var(--green-light);box-shadow:0 0 0 2px var(--green);display:flex;align-items:center;justify-content:center;text-align:center;font-size:8.4px;line-height:11.4px;padding:10px;color:#222}
.services{left:28px;top:398px;list-style:none}
.services li{position:relative;padding-left:23px;font-size:15.5px;line-height:21.5px;margin-bottom:3px;color:var(--ink);font-weight:300;white-space:nowrap}
.services li::before{content:"";position:absolute;left:0;top:4px;width:15px;height:11px;background:var(--green);border-radius:0 100% 0 100%}
.extras{left:28px;top:544px;font-size:17px;line-height:22px;color:var(--green-text);font-weight:400}
.extras p+p{margin-top:7px}
.call{left:28px;top:640px;font-size:15px;font-weight:300;color:var(--ink)}
.call strong{font-family:"Oswald",Arial,sans-serif;font-weight:700;font-size:19px}
.cover-url{left:28px;top:671px;font-size:14px;letter-spacing:.7px;color:var(--green-dark)}
.care-panel{left:285px;top:413px;width:182px;height:298px;border-radius:80px 80px 0 0;background:var(--green)}
.figure-man{left:226px;top:449px;width:70px;height:262px;border-radius:35px 35px 6px 6px;background:linear-gradient(180deg,#2b2b2b 0%,#2f5ea8 35%,#1b1b1b 70%,#9aa0a6 100%)}
.figure-woman{left:454px;top:469px;width:50px;height:242px;border-radius:25px 25px 6px 6px;background:linear-gradient(180deg,#2a2a2a 0%,#3a3a3a 50%,#1a1a1a 100%)}
.care-copy{left:300px;top:428px;width:152px;text-align:center;color:var(--white)}
.care-copy h2{font-size:20px;line-height:25px;font-weight:700}
.care-copy p{margin-top:8px;font-size:11.4px;line-height:17.6px;font-weight:400}
</style>
</head>
<body>

<section class="page page--info">
  <div class="abs site-url">www.harborstridegym.com.au</div>
  <div class="abs photo photo--physio" role="img" aria-label="Physiotherapist treating a client's back"></div>
  <div class="abs photo photo--lifting" role="img" aria-label="Muscular man training on a cable machine"></div>
  <div class="abs photo photo--food" role="img" aria-label="Dumbbell, vegetables, tape measure and water bottle"></div>

  <div class="abs bio bio--owner">
    <p>The owner of the Studio, Daniel Marsh, has over 20 years of experience in personal exercise care and is a registered Exercise Physiologist with Allied Movement Council (AMC). He has completed a Masters of Health Science (Exercise Science), as well as a Masters in Clinical Exercise Physiology (Rehabilitation).</p>
    <p>The studio has an approach to exercise, which has health at the centre of all physical training programs. It was originally set up within the Northside Community Hospital at Kellaway in 1998, with the intention of providing an exercise clinic for inpatients and outpatients of the hospital.</p>
  </div>
  <div class="abs bio bio--specialist">
    <p>Clara Benton is an exercise specialist at the studio, with expertise in weight management and in coaching individuals towards life-long lifestyle change. When the challenge ahead is arduous, it is important to have the right person working with you along the way. Clara is committed and determined to assisting you in the achievement of your objectives.</p>
    <p>Harbor Stride Gym looks after individuals of all ages and all levels of health and fitness. The Studio is experienced at designing lifestyle plans for people who are starting from a very low level of health and fitness, or who have challenging health issues.</p>
  </div>

  <div class="abs illus-woman" role="img" aria-label="Woman in pink top sitting cross-legged holding a dumbbell and a plate of vegetables"></div>
  <div class="abs tagline">Your Pathway to Lifelong Change!</div>
  <div class="abs brand"><span class="brand__dot"></span>Harbor Stride Gym</div>

  <p class="abs pitch">Long-term lifestyle<br>change requires attention to the many<br>areas of life that impact on your health<br>and fitness. Our experience and expertise<br>in this area will guide you through<br>this challenging process.</p>

  <div class="abs contact">
    <div class="contact__label">Mobile:</div>
    <div class="contact__phone">0412 555 018 (Daniel)<br>0455 555 027 (Clara)</div>
    <div class="contact__mail">daniel@harborstridegym.com.au<br>clara@harborstridegym.com.au</div>
    <div class="contact__rule"></div>
    <div class="contact__addr">Suite 4/ 12 Carrow Lane, Belrose</div>
  </div>
</section>

<section class="page page--cover">
  <svg class="abs hero" viewBox="0 0 504 370" aria-hidden="true">
    <defs>
      <linearGradient id="photo-tone" x1="0" y1="0" x2="1" y2="1">
        <stop offset="0" stop-color="#ffffff"/>
        <stop offset="0.55" stop-color="#f1e7dc"/>
        <stop offset="1" stop-color="#c9d4e4"/>
      </linearGradient>
    </defs>
    <rect x="0" y="0" width="504" height="350" fill="var(--green)"/>
    <path d="M0 0 H360 C200 30 50 140 22 330 L0 330 Z" fill="var(--green-dark)"/>
    <path d="M28 305 C8 220 70 110 190 55 C280 15 380 5 420 40 C445 80 440 200 420 270 C400 320 370 335 330 340 C220 352 90 345 28 305 Z" fill="url(#photo-tone)"/>
    <path d="M0 318 C120 356 280 362 504 334 V370 H0 Z" fill="var(--paper-grey)"/>
    <path d="M0 312 C120 350 280 356 504 326" fill="none" stroke="var(--green-dark)" stroke-width="5"/>
    <path d="M0 326 C130 360 280 364 470 342" fill="none" stroke="var(--green-light)" stroke-width="2"/>
  </svg>
  <div class="abs hero-photo" role="img" aria-label="Smiling older woman stretching on a blue exercise mat"></div>

  <div class="abs hero-script">Your Pathway to<br>Lifelong<br>Change!</div>
  <div class="abs cover-brand">Harbor Stride<br>Gym</div>
  <h1 class="abs headline">Personalised care in fitness and health</h1>
  <div class="abs hours">the studio is open from 5:30am until 8pm</div>
  <div class="abs badge">Exercise provides the natural, physical medicine to assist in the treatment and care of numerous conditions.</div>

  <ul class="abs services">
    <li>One On One<br>Consultation</li>
    <li>Assessment</li>
    <li>A Personalised Program</li>
    <li>Personal Training</li>
  </ul>
  <div class="abs extras">
    <p>NUTRITIONAL CARE</p>
    <p>ONGOING LIFESTYLE<br>GUIDANCE</p>
  </div>
  <div class="abs call">Call us <strong>(02) 5550 1846</strong></div>
  <div class="abs cover-url">harborstridegym.com.au</div>

  <div class="abs care-panel"></div>
  <div class="abs figure-man" role="img" aria-label="Fit man in blue shirt standing with an exercise ball"></div>
  <div class="abs figure-woman" role="img" aria-label="Athletic woman in sportswear standing with hands on hips"></div>
  <div class="abs care-copy">
    <h2>Personalised Lifestyle Care</h2>
    <p>Harbor Stride Gym is a professional exercise clinic which was established at Belrose in 2005, to service the fitness and health needs of the community.</p>
  </div>
</section>

</body>
</html>
```